Juice Label for Hispanic Customer Demographic

We need a label design for two related Juice items. Brand name will be "Cidrovel" The first item is a Lemon Juice Blend and the second is a lime juice. We would like to see designs that focus on a target market that is mainly first and second generation Hispanic immigrants. Heavily Spanish speaking and price conscious.

Product will be packaged in 32 oz flip to bottle with wrap around label. Both SKU’s will have the same size and design with one showing Lemons and the other showing Limes similar to the examples attached. The bottle will be green with a green cap for the lime juice and a yellow cap for the lemon juice.

I have attached Dielines and some images of a similar product for reference.

Target Market(s)

Hispanic shopper, mainly first and second generation immigrants. Heavily Spanish speaking demographic. Price conscious.

Industry/Entity Type

Grocery Store

Font styles to use
Sans Serif

Colors
ffcf3e
abd036
fbf289
fbee3e

Requirements
Must have
• Product Name—
• • “Cidrovel Lemon Juice Blend” -- 54% Juice
• • “Cidrovel Lime Juice “-- 25% Juice
• Please include copy-
• Note: Product name and required copy below should be in English. Additional copy can be either English or Spanish.
• • “Made in the USA”
• • “From Concentrate”
• • “Naturally Reconstituted”
• • “Refrigerate after opening”
• • “Shake Well!”
• • “Net 32 Fl OZ (1QT) 946 ml”
• Please include a space for the nutrition facts should be :
• 4 8/10 cm H x 3 8/10 cm W.
• Include a white space for the scan bar 1/7/10 cm H x 3/2/10 cm W. (?? Dimensions)
• Please use ingredient lists as below-
• Lemon Juice--
• INGREDIENTS: FILTERED WATER, LEMON
• JUICE CONCENTRATE, CITRIC ACID, ESTER
• GUM, LEMON OIL, SODIUM BENZOATE (AS
• PRESERVATIVE), SODIUM BISULFITE (AS
• PRESERVATIVE).
• Lime Juice--
• INGREDIENTS: FILTERED WATER, LIME JUICE CONCENTRATE, CITRIC ACID,
• ESTER GUM, LIME OIL, SODIUM BENZOATE (AS PRESERVATIVE), SODIUM BISULFITE (AS A PRESERVATIVE)
Nice to have
• Would like to have an image of fruit very prominent in the design. This image can be either a drawing or a photograph.

```html
<!DOCTYPE html>
<html lang="en">
<head>
<meta charset="utf-8">
<title>Cidrovel Juice Labels</title>
<link rel="stylesheet" href="https://fonts.googleapis.com/css2?family=Lustria&family=Oswald:wght@500&family=Kaushan+Script&family=Roboto+Condensed:wght@500&display=swap">
<style>
  :root {
    --canvas-bg: #ecebe6;
    --brand-green: #1f7a2e;
    --banner-green: #1e8a3a;
    --banner-edge: #7cc26a;
    --white: #ffffff;
    --lemon-top: #fbee3e;
    --lemon-mid: #ffcf3e;
    --lemon-bottom: #f39a1e;
    --lemon-frame: #ee8a1c;
    --lime-top: #d9ea8a;
    --lime-mid: #abd036;
    --lime-bottom: #8cc63f;
    --lime-frame: #3f9a3a;
    --ink-dark: #1c2a12;
  }
  * { margin: 0; padding: 0; box-sizing: border-box; }
  html, body { width: 900px; height: 1200px; overflow: hidden; }
  body {
    background: var(--canvas-bg);
    display: flex;
    flex-direction: column;
    align-items: center;
    justify-content: center;
    gap: 34px;
  }
  .label { width: 640px; height: 549px; display: block; box-shadow: 0 2px 10px rgba(0,0,0,0.12); }
  .brand-name { font-family: "Lustria", serif; font-size: 54px; fill: var(--brand-green); }
  .product-name { font-family: "Lustria", serif; font-size: 19px; fill: var(--white); }
  .juice-percent { font-family: "Oswald", sans-serif; font-weight: 500; font-size: 44px; }
  .percent-sign { font-family: "Oswald", sans-serif; font-weight: 500; font-size: 16px; }
  .juice-word { font-family: "Kaushan Script", cursive; font-size: 24px; }
  .net-content { font-family: "Roboto Condensed", sans-serif; font-weight: 500; font-size: 11.5px; fill: var(--ink-dark); }
</style>
</head>
<body>

  <!-- Lemon Juice Blend label -->
  <svg class="label label--lemon" viewBox="0 0 420 360" xmlns="http://www.w3.org/2000/svg">
    <defs>
      <linearGradient id="lemon-bg" x1="0" y1="0" x2="0" y2="1">
        <stop offset="0" stop-color="var(--lemon-top)"/>
        <stop offset="0.45" stop-color="var(--lemon-mid)"/>
        <stop offset="1" stop-color="var(--lemon-bottom)"/>
      </linearGradient>
      <linearGradient id="lemon-fruit" x1="0" y1="0" x2="1" y2="1">
        <stop offset="0" stop-color="#fde66a"/>
        <stop offset="1" stop-color="#f2c21e"/>
      </linearGradient>
      <linearGradient id="lemon-splash" x1="0" y1="0" x2="1" y2="0">
        <stop offset="0" stop-color="#ffffff" stop-opacity="0.9"/>
        <stop offset="1" stop-color="#f7d77a" stop-opacity="0.8"/>
      </linearGradient>
    </defs>
    <rect class="label-bg" width="420" height="360" fill="url(#lemon-bg)"/>
    <path class="name-panel" d="M22,235 L22,112 Q22,88 50,88 Q56,64 92,66 Q122,46 152,54 Q182,34 212,36 Q244,34 270,54 Q302,46 330,66 Q364,64 372,88 Q398,88 398,112 L398,190 C330,210 250,232 170,244 C110,252 52,250 22,235 Z"
          fill="var(--white)" stroke="var(--lemon-frame)" stroke-width="4"/>
    <path class="juice-splash" role="img" aria-label="Flowing lemon juice splash"
          d="M20,240 C120,255 250,225 420,160 L420,195 C270,250 140,275 20,262 Z" fill="url(#lemon-splash)"/>
    <text class="brand-name" x="210" y="164" text-anchor="middle">Cidrovel</text>
    <rect class="product-banner" x="116" y="174" width="188" height="38" fill="var(--banner-green)" stroke="var(--banner-edge)" stroke-width="2"/>
    <text class="product-name" x="210" y="199" text-anchor="middle">Lemon Juice Blend</text>
    <rect class="fruit-art" role="img" aria-label="Illustration of whole lemons, a halved lemon and green leaves"
          x="0" y="238" width="300" height="100" rx="40" fill="url(#lemon-fruit)"/>
    <circle class="juice-badge" cx="382" cy="290" r="52" fill="var(--lemon-bottom)" stroke="var(--white)" stroke-width="3"/>
    <text class="juice-percent" x="346" y="298" fill="var(--white)">54</text>
    <text class="percent-sign" x="390" y="268" fill="var(--white)">%</text>
    <text class="juice-word" x="346" y="324" fill="var(--white)">juice</text>
    <text class="net-content" x="412" y="352" text-anchor="end">Net 32 Fl OZ (1QT) 946 ml</text>
  </svg>

  <!-- Lime Juice label -->
  <svg class="label label--lime" viewBox="0 0 420 360" xmlns="http://www.w3.org/2000/svg">
    <defs>
      <linearGradient id="lime-bg" x1="0" y1="0" x2="0" y2="1">
        <stop offset="0" stop-color="var(--lime-top)"/>
        <stop offset="0.45" stop-color="var(--lime-mid)"/>
        <stop offset="1" stop-color="var(--lime-bottom)"/>
      </linearGradient>
      <linearGradient id="lime-fruit" x1="0" y1="0" x2="1" y2="1">
        <stop offset="0" stop-color="#7fc35a"/>
        <stop offset="1" stop-color="#2f8a3a"/>
      </linearGradient>
      <linearGradient id="lime-splash" x1="0" y1="0" x2="1" y2="0">
        <stop offset="0" stop-color="#ffffff" stop-opacity="0.9"/>
        <stop offset="1" stop-color="#cfe58a" stop-opacity="0.8"/>
      </linearGradient>
    </defs>
    <rect class="label-bg" width="420" height="360" fill="url(#lime-bg)"/>
    <path class="name-panel" d="M22,235 L22,112 Q22,88 50,88 Q56,64 92,66 Q122,46 152,54 Q182,34 212,36 Q244,34 270,54 Q302,46 330,66 Q364,64 372,88 Q398,88 398,112 L398,190 C330,210 250,232 170,244 C110,252 52,250 22,235 Z"
          fill="var(--white)" stroke="var(--lime-frame)" stroke-width="4"/>
    <path class="juice-splash" role="img" aria-label="Flowing lime juice splash"
          d="M20,240 C120,255 250,225 420,160 L420,195 C270,250 140,275 20,262 Z" fill="url(#lime-splash)"/>
    <text class="brand-name" x="210" y="164" text-anchor="middle">Cidrovel</text>
    <rect class="product-banner" x="126" y="174" width="168" height="38" fill="var(--banner-green)" stroke="var(--banner-edge)" stroke-width="2"/>
    <text class="product-name" x="210" y="199" text-anchor="middle">Lime Juice</text>
    <rect class="fruit-art" role="img" aria-label="Illustration of whole limes, a lime wedge and a leaf"
          x="0" y="220" width="290" height="118" rx="45" fill="url(#lime-fruit)"/>
    <circle class="juice-badge" cx="382" cy="290" r="52" fill="var(--lime-top)" stroke="var(--lime-frame)" stroke-width="3"/>
    <text class="juice-percent" x="346" y="298" fill="var(--lime-frame)">25</text>
    <text class="percent-sign" x="390" y="268" fill="var(--lime-frame)">%</text>
    <text class="juice-word" x="346" y="324" fill="var(--lime-frame)">juice</text>
    <text class="net-content" x="412" y="352" text-anchor="end">Net 32 Fl OZ (1QT) 946 ml</text>
  </svg>

</body>
</html>
```